Web Design for Harbor Lane Guild

We need a web design for Harbor Lane Guild. You can see more details about the kind of business that it deals with in this link: http://harborlaneguild.example/. The concept of the site is similar to http://www.kelvora.example/ and we are looking for a homepage design also similar to it.
The top navigation should have:
1) directory
2) articles
3) deals
4) forums
5) log in/register page.
It should also have a video, a slider, map & text as well as a call to action to a "why register page".
As part of the footer it should include:
1) about HLG
2) contact HGL
3) terms & conditions
4) privacy
The color palette for the site will be the UAE flag colors which are red, green, white and black.
Updates
Project Deadline Extended
Reason: We need more designs and options.
Keep sending in more creative designs. thanks.
Industry/Entity Type
Business
Look and feel
Each slider illustrates characteristics of the customer's brand and the style your logo design should communicate.

```html
<!DOCTYPE html>
<html lang="en">
<head>
<meta charset="utf-8">
<title>Harbor Lane Guild – Home</title>
<link rel="stylesheet" href="https://fonts.googleapis.com/css2?family=Lato:wght@400;700&display=swap">
<style>
:root{
  --green:#1f9a46;
  --red:#e8321f;
  --red-dark:#c92513;
  --ink:#333333;
  --ink-soft:#444444;
  --grey-band:#ececec;
  --grey-light:#f1f1f1;
  --footer:#1c1c1c;
  --white:#ffffff;
}
*{margin:0;padding:0;box-sizing:border-box}
html,body{width:1122px;height:1200px;overflow:hidden;background:var(--white);font-family:'Lato',sans-serif;color:var(--ink)}
.page{position:relative;width:1122px;height:1200px}
.wrap{position:absolute;left:150px;width:822px}

/* header */
.site-header{position:absolute;top:0;left:0;width:100%;height:107px;background:var(--white);border-bottom:2px solid #d4d4d4}
.brand{position:absolute;left:150px;top:36px;display:flex;align-items:center;gap:8px;font-size:17px;font-weight:700;color:var(--red);letter-spacing:.2px}
.brand-mark{width:22px;height:22px;border-radius:50%;background:var(--green)}
.main-nav{position:absolute;right:150px;top:49px;display:flex;gap:23px;font-size:13.5px}
.main-nav a{color:var(--ink);text-decoration:none;position:relative}
.main-nav a.is-active{color:var(--green)}
.main-nav a.is-active::before{content:"";position:absolute;left:-1px;right:-1px;top:-49px;height:4px;background:var(--green)}
.main-nav a.is-accent{color:var(--red)}

/* hero slider */
.hero{position:absolute;top:107px;left:0;width:100%;height:279px;background:linear-gradient(120deg,#b9b9b9 0%,#e2e2e2 35%,#d2d2d2 60%,#f0f0f0 80%,#c9c9c9 100%);overflow:hidden}
.hero-arc{position:absolute;left:0;top:0}
.hero-copy{position:absolute;left:140px;top:80px;width:290px;text-align:right}
.hero-title{font-size:21px;font-weight:400;color:var(--white);margin-bottom:8px}
.hero-title span{color:var(--red)}
.hero-text{font-size:13px;line-height:18.3px;color:var(--ink)}
.slider-dots{position:absolute;right:692px;top:195px;display:flex;gap:4px}
.slider-dots i{width:10px;height:10px;background:#8d8d8d}
.slider-dots i.is-current{background:var(--white)}
.hero-photo{position:absolute;left:482px;top:24px;width:490px;height:255px;background:linear-gradient(180deg,#9a9a9a 0%,#4a4a4a 55%,#2a2a2a 100%);border-radius:120px 120px 0 0}

/* call to action band */
.cta-band{position:absolute;top:386px;left:0;width:100%;height:55px;background:linear-gradient(180deg,#f4f4f4,#e3e3e3)}
.cta-text{position:absolute;left:262px;top:18px;font-size:16.5px;color:var(--ink)}
.cta-button{position:absolute;left:637px;top:11px;width:189px;height:34px;background:var(--red);border-bottom:2px solid var(--red-dark);color:var(--white);font-size:14.5px;display:flex;align-items:center;justify-content:center;gap:7px;text-decoration:none}

/* mission */
.video{position:absolute;left:150px;top:480px;width:341px;height:227px;background:linear-gradient(135deg,#d9d9d9 0%,#8a8a8a 60%,#3d3d3d 100%)}
.video-bar{position:absolute;left:0;bottom:0;width:100%;height:30px;background:rgba(40,40,40,.85);display:flex;align-items:center;color:var(--white);font-size:13px}
.video-play{width:43px;height:30px;background:rgba(20,20,20,.9);display:flex;align-items:center;justify-content:center;margin-right:11px}
.mission{position:absolute;left:511px;top:476px;width:461px}
.mission h2{font-size:17px;font-weight:700;color:var(--green);margin-bottom:10px}
.mission ul{list-style:none}
.mission li{position:relative;padding-left:21px;font-size:12.3px;line-height:15px;color:var(--ink-soft);margin-bottom:14.5px}
.mission li::before{content:"";position:absolute;left:5px;top:3px;width:8px;height:8px;background:var(--green);box-shadow:-2px 2px 0 var(--red)}

/* contact */
.contact{position:absolute;top:770px;left:0;width:100%;height:316px;background:var(--grey-light)}
.address{position:absolute;left:150px;top:36px;width:341px}
.address h3{font-size:13.5px;font-weight:400;color:var(--ink);padding-bottom:7px;border-bottom:1px dashed #b5b5b5;margin-bottom:12px;letter-spacing:.2px}
.address p{font-size:13px;line-height:18.2px;color:var(--ink-soft)}
.partner-badge{position:absolute;left:150px;top:200px;width:341px;height:77px;background:var(--white);border:1px solid #cfcfcf;border-radius:3px}
.map{position:absolute;left:517px;top:40px;width:454px;height:235px;border:5px solid var(--white);background:linear-gradient(135deg,#e8e2d8,#d8d2c6)}

/* footer */
.site-footer{position:absolute;top:1086px;left:0;width:100%;height:114px;background:var(--footer);border-top:3px solid #555}
.footer-left{position:absolute;left:150px;top:54px;font-size:12px;color:#d8d8d8;display:flex;align-items:center;gap:6px}
.social{display:inline-block;width:12px;height:12px;border-radius:50%;background:#8a8a8a;margin-left:4px}
.footer-nav{position:absolute;right:152px;top:54px;display:flex;gap:11px;font-size:12px}
.footer-nav a{color:#d8d8d8;text-decoration:none}
</style>
</head>
<body>
<div class="page">

  <header class="site-header">
    <div class="brand"><span class="brand-mark"></span>Harbor Lane Guild</div>
    <nav class="main-nav">
      <a href="#" class="is-active">HOME</a>
      <a href="#">DIRECTORY</a>
      <a href="#">ARTICLES</a>
      <a href="#">DEALS</a>
      <a href="#">FORUMS</a>
      <a href="#" class="is-accent">LOG IN</a>
      <a href="#" class="is-accent">REGISTER PAGE</a>
    </nav>
  </header>

  <section class="hero">
    <svg class="hero-arc" width="1122" height="279" viewBox="0 0 1122 279" aria-hidden="true">
      <path d="M0 279 Q200 60 520 0 L560 0 Q260 90 80 279 Z" fill="#ffffff" opacity=".25"/>
      <path d="M1122 0 Q1050 180 980 279 L1122 279 Z" fill="#ffffff" opacity=".3"/>
    </svg>
    <div class="hero-copy">
      <h1 class="hero-title"><span>Welcome</span> to our site</h1>
      <p class="hero-text">An online business networking platform exclusively for UAE Freezone Companies, Where they can learn, communicate effectively and benefit from working with each other.</p>
    </div>
    <div class="slider-dots"><i class="is-current"></i><i></i><i></i></div>
    <div class="hero-photo" role="img" aria-label="Photo of four smiling business professionals in dark suits"></div>
  </section>

  <section class="cta-band">
    <p class="cta-text">BE PART OF THIS INCREDIBLE NETWORK!</p>
    <a class="cta-button" href="#">WHY REGISTER PAGE
      <svg width="7" height="11" viewBox="0 0 7 11" aria-hidden="true"><path d="M0 0 L7 5.5 L0 11 Z" fill="#ffffff"/></svg>
    </a>
  </section>

  <div class="video" role="img" aria-label="Video still of a businessman in a suit">
    <div class="video-bar">
      <span class="video-play"><svg width="12" height="14" viewBox="0 0 12 14" aria-hidden="true"><path d="M0 0 L12 7 L0 14 Z" fill="#ffffff"/></svg></span>
      SEE OUR PROJECT VIDEO
    </div>
  </div>

  <section class="mission">
    <h2>OUR MISSION :</h2>
    <ul>
      <li>Harbor Lane Guild will allow you to maximize the potential of your Free Zone business.</li>
      <li>A business Networking Platform helping Free Zone members' source new customers.</li>
      <li>Provide a supportive infrastructure to enable companies to access and engage in unlimited networking opportunities.</li>
      <li>Build mutual business relationships with fellow Free Zone companies.</li>
      <li>As a Harbor Lane Guild member, you will have the opportunity to improve business techniques, whilst collaborating with industry peers and fellow professionals.</li>
      <li>The Harbor Lane Guild keeps you up to date with what's happening and where.</li>
    </ul>
  </section>

  <section class="contact">
    <div class="address">
      <h3>ADDRESS</h3>
      <p>Level 12, Quayside Court, Tower 3, Marlow Crescent Avenue,<br>Harbor District, P.O. Box 501287, Portvale, United Arab Emirates<br>T: +971 (4) 555 0142 | F: +971 (4) 555 0187<br>E: nadia@harborlaneguild.example</p>
    </div>
    <div class="partner-badge" role="img" aria-label="Partner project badge"></div>
    <div class="map" role="img" aria-label="Street map showing the office location"></div>
  </section>

  <footer class="site-footer">
    <div class="footer-left">Copyright@2013, HarborLaneGuild &nbsp;|&nbsp; Follow Us : <span class="social" role="img" aria-label="Social link"></span><span class="social" role="img" aria-label="Social link"></span></div>
    <nav class="footer-nav">
      <a href="#">About HLG</a>
      <a href="#">Contact HGL</a>
      <a href="#">Terms &amp; Conditions</a>
      <a href="#">Privacy</a>
    </nav>
  </footer>

</div>
</body>
</html>
```